IT services company requires Letterhead design

We need a professional letterhead designed to be used for general correspondence with customers, quotes, invoices etc. We are a new IT services company specialising in computer servicing and repairs and mobile and tablet repairs. Attached are templates that my printing company have supplied, my logos, an interpretation of our website for you to get a feel of the company. Details to be included on the letterhead are

Company Number – 4830517
VAT Number - 581736294
Registered Address – 14-16 Brambury Lane, London, E9 3PL

Phone – 01843 572236
Email – sales@quorvant.com
Web – www.quorvant.com

I would prefer for the top of the letterhead to just have the company logo on a white background and the rest of the details on the bottom of the letterhead but I am open to design ideas.

Thanks

```html
<!DOCTYPE html>
<html lang="en">
<head>
<meta charset="utf-8">
<title>Quorvant Letterhead</title>
<link rel="stylesheet" href="https://fonts.googleapis.com/css2?family=Jost:wght@400;600&family=Arimo:wght@400;700&display=swap">
<style>
  :root {
    --backdrop: #e6e6e6;
    --paper: #ffffff;
    --cyan: #2ec0e4;
    --ink: #3a3a3c;
    --text: #555557;
    --rule: #3a3a3c;
  }
  * { box-sizing: border-box; margin: 0; padding: 0; }
  html, body { width: 1200px; height: 1200px; overflow: hidden; background: var(--backdrop); }
  .letterhead {
    position: absolute; left: 204px; top: 40px;
    width: 792px; height: 1120px;
    background: var(--paper);
    box-shadow: 0 2px 8px rgba(0,0,0,0.08);
    overflow: hidden;
    font-family: "Arimo", Arial, sans-serif;
    color: var(--text);
  }
  .corner-mark { position: absolute; left: 56px; top: 0; }
  .brand {
    position: absolute; left: 72px; top: 96px;
    display: flex; align-items: center; gap: 10px;
    font-family: "Jost", sans-serif; font-weight: 600;
    font-size: 42px; line-height: 1; color: var(--ink); letter-spacing: 0.5px;
  }
  .brand-square { width: 10px; height: 10px; background: var(--cyan); }
  .company-info {
    position: absolute; left: 330px; top: 38px;
    border-left: 2px solid var(--rule);
    padding-left: 12px;
    font-family: "Jost", sans-serif; font-size: 12.5px; line-height: 18px;
    color: var(--ink);
  }
  .company-info .label { color: var(--cyan); }
  .contact-info {
    position: absolute; left: 540px; top: 26px;
    border-left: 2px solid var(--rule);
    padding-left: 12px;
    font-family: "Jost", sans-serif; font-size: 12.5px; line-height: 18px;
    color: var(--ink);
    list-style: none;
  }
  .contact-info li { display: flex; gap: 10px; align-items: flex-start; }
  .contact-info svg { flex: none; margin-top: 3px; }
  .letter-body {
    position: absolute; left: 96px; top: 300px; width: 600px;
    font-size: 11px; line-height: 14px;
  }
  .salutation { margin-bottom: 22px; }
  .letter-body p + p { margin-top: 18px; }
  .sign-off { position: absolute; left: 96px; top: 800px; font-size: 11px; }
  .signatory { font-weight: 700; color: var(--ink); }
  .signature { display: block; width: 120px; height: 36px; margin: 8px 0 6px 6px; }
  .footer-band { position: absolute; left: 0; bottom: 0; width: 100%; }
  .footer-band .rule { height: 4px; background: var(--rule); }
  .footer-band .fill { height: 28px; background: var(--cyan); }
</style>
</head>
<body>
  <main class="letterhead">
    <svg class="corner-mark" width="40" height="26" viewBox="0 0 40 26" aria-hidden="true">
      <polygon points="0,0 40,0 26,26" fill="var(--cyan)"/>
    </svg>

    <div class="brand"><span class="brand-square"></span>Quorvant</div>

    <div class="company-info">
      <div>www.quorvant.com</div>
      <div><span class="label">VAT Number</span> - 581736294</div>
      <div><span class="label">Company Number</span> – 4830517</div>
    </div>

    <ul class="contact-info">
      <li>
        <svg width="10" height="10" viewBox="0 0 24 24"><path fill="var(--cyan)" d="M6.6 10.8a15 15 0 0 0 6.6 6.6l2.2-2.2a1 1 0 0 1 1-.25 11.4 11.4 0 0 0 3.6.57 1 1 0 0 1 1 1V20a1 1 0 0 1-1 1A17 17 0 0 1 3 4a1 1 0 0 1 1-1h3.5a1 1 0 0 1 1 1c0 1.25.2 2.45.57 3.57a1 1 0 0 1-.25 1z"/></svg>
        <span>01843 572236</span>
      </li>
      <li>
        <svg width="10" height="10" viewBox="0 0 24 24"><path fill="var(--cyan)" d="M2 5h20v14H2z M2 5l10 8 10-8" stroke="#fff" stroke-width="1.5"/></svg>
        <span>sales@quorvant.com</span>
      </li>
      <li>
        <svg width="10" height="10" viewBox="0 0 24 24"><path fill="var(--cyan)" d="M12 2a7 7 0 0 0-7 7c0 5 7 13 7 13s7-8 7-13a7 7 0 0 0-7-7zm0 9.5A2.5 2.5 0 1 1 12 6.5a2.5 2.5 0 0 1 0 5z"/></svg>
        <span>14-16 Brambury Lane,<br>London, E9 3PL</span>
      </li>
    </ul>

    <section class="letter-body">
      <p class="salutation">Dear Sir,</p>
      <p>Lorem Ipsum is simply dummy text of the printing and typesetting industry. Lorem Ipsum has been the industry's standard dummy text ever since the 1500s, when an unknown printer took a galley of type and scrambled it to make a type specimen book. It has survived not only five centuries, but also the leap into electronic typesetting, remaining essentially unchanged. It was popularised in the 1960s with the release of Typeline sheets containing Lorem Ipsum passages, and more recently with desktop publishing software like Folio Composer including versions of Lorem Ipsum.</p>
      <p>Lorem Ipsum is simply dummy text of the printing and typesetting industry. Lorem Ipsum has been the industry's standard dummy text ever since the 1500s, when an unknown printer took a galley of type and scrambled it to make a type specimen book. It has survived not only five centuries, but also the leap into electronic typesetting.</p>
      <p>Lorem Ipsum is simply dummy text of the printing and typesetting industry. Lorem Ipsum has been the industry's standard dummy text ever since the 1500s, when an unknown printer took a galley of type and scrambled it to make a type.</p>
      <p>Lorem Ipsum is simply dummy text of the printing and typesetting industry. Lorem Ipsum has been the industry's standard dummy text ever since the 1500s, when an unknown printer took a galley of type and scrambled it to make a type specimen book. It has survived not only five centuries, but also the leap into electronic typesetting, remaining essentially unchanged. It was popularised in the 1960s with the release of Typeline sheets containing Lorem Ipsum passages, and more recently with desktop publishing software like Folio Composer including versions of Lorem Ipsum. Lorem Ipsum is simply dummy text of the printing and typesetting industry. Lorem Ipsum has been the industry's standard dummy text ever since the 1500s, when an unknown printer took a galley of type and scrambled it to make a type specimen book. It has survived not only five centuries, but also the leap into electronic typesetting.</p>
      <p>Lorem Ipsum is simply dummy text of the printing and typesetting industry. Lorem Ipsum has been the industry's standard dummy text ever since the 1500s, when an unknown printer took a galley of type and scrambled it to make a type.</p>
    </section>

    <div class="sign-off">
      <div class="signatory">Daniel Foster</div>
      <svg class="signature" role="img" aria-label="Handwritten signature of Daniel Foster" viewBox="0 0 120 36">
        <rect width="120" height="36" rx="4" fill="#dff3f9"/>
      </svg>
      <div class="role">Director</div>
    </div>

    <div class="footer-band">
      <div class="rule"></div>
      <div class="fill"></div>
    </div>
  </main>
</body>
</html>
```